Lumara Health & Wellness Business Card Design

We would like to create business cards matching with our new logo design. The card should be professional looking but still have a playful side and something that would be eye catching. We are planing to open a luxury medical spa and looking to create a design based on this new logo. We are looking for a design that shows off luxury but not be gold in color. Also, while we are a more female oriented medical center we do have men that come in for our services and it should be be too feminine.

Target Market(s)

Health & Wellness. Medical patients. Luxury spa

Industry/Entity Type

Health And Wellness

Contact Information for Business Card

It should have the logo design in the front of card and back of card should have our contact information. Our current colors are peach/ coral, teal, and gray. We are looking for a modern looking design.

Font styles to use
Script

Colors
32a6d6
e667a6
86cfc6
fece3e

Requirements
Must have
• It should have our logo design. We would prefer to have a more modern look to the card.
Nice to have
• Eye-Catching Design on the personable side but still classy.
Should not have
• At this point we are looking for the best design. It should not have color purple.

```html
<!DOCTYPE html>
<html lang="en">
<head>
<meta charset="utf-8">
<title>Lumara Health &amp; Wellness — Business Card</title>
<link rel="stylesheet" href="https://fonts.googleapis.com/css2?family=Roboto:wght@300;400;500;700&display=swap">
<style>
  :root {
    --backdrop: #e6e7e6;
    --card: #ffffff;
    --coral: #ea7761;
    --teal: #7fd3c5;
    --ink: #3b3b3b;
    --rule: #d4d4d4;
  }
  * { box-sizing: border-box; margin: 0; padding: 0; }
  html, body {
    width: 1200px; height: 814px; overflow: hidden;
    background: var(--backdrop);
    font-family: "Roboto", Arial, sans-serif;
  }
  .canvas {
    position: relative; width: 1200px; height: 814px;
    display: flex; align-items: center; justify-content: center; gap: 40px;
  }
  .card {
    position: relative; width: 520px; height: 297px;
    background: var(--card);
    border-bottom: 6px solid var(--coral);
    box-shadow: 0 10px 24px rgba(0,0,0,0.10);
  }
  .brand { color: var(--coral); font-weight: 300; text-align: center; line-height: 1.1; }
  .brand__name { display: block; font-size: 44px; letter-spacing: 1px; }
  .brand__line { display: block; font-size: 15px; letter-spacing: 2.5px; text-transform: uppercase; margin-top: 6px; }

  /* Front */
  .card--front { display: flex; flex-direction: column; align-items: center; justify-content: center; }
  .card--front .web {
    margin-top: 30px; font-size: 13px; letter-spacing: 4px; color: var(--ink);
  }

  /* Back */
  .card--back .brand { position: absolute; left: 30px; top: 98px; width: 230px; }
  .card--back .brand__name { font-size: 38px; }
  .card--back .brand__line { font-size: 12px; letter-spacing: 1.8px; }
  .divider {
    position: absolute; left: 280px; top: 34px; width: 1px; height: 150px;
    background: linear-gradient(var(--card), var(--rule) 30%, var(--rule) 70%, var(--card));
  }
  .contact { position: absolute; left: 300px; top: 36px; }
  .contact__name { color: var(--coral); font-weight: 700; font-size: 19px; letter-spacing: 0.5px; }
  .contact__role { color: var(--teal); font-size: 13px; letter-spacing: 0.8px; margin-bottom: 10px; }
  .contact__list { list-style: none; }
  .contact__item {
    display: flex; align-items: center; gap: 8px;
    font-size: 12.5px; color: var(--ink); line-height: 21px;
  }
  .icon { width: 12px; height: 12px; fill: var(--coral); flex: none; }
  .address {
    position: absolute; left: 40px; right: 20px; bottom: 36px;
    display: flex; align-items: center; justify-content: center; gap: 8px;
    font-size: 14px; color: var(--ink);
  }
  .address .icon { width: 13px; height: 15px; }
</style>
</head>
<body>
<main class="canvas">
  <section class="card card--front" aria-label="Card front">
    <div class="brand">
      <span class="brand__name">Lumara</span>
      <span class="brand__line">Health &amp; Wellness</span>
    </div>
    <p class="web">www.lumarawellness.com</p>
  </section>

  <section class="card card--back" aria-label="Card back">
    <div class="brand">
      <span class="brand__name">Lumara</span>
      <span class="brand__line">Health &amp; Wellness</span>
    </div>
    <div class="divider"></div>
    <div class="contact">
      <p class="contact__name">NADIA REYES</p>
      <p class="contact__role">CEO/FOUNDER</p>
      <ul class="contact__list">
        <li class="contact__item">
          <svg class="icon" viewBox="0 0 24 24"><path d="M6.6 10.8a15.1 15.1 0 0 0 6.6 6.6l2.2-2.2a1 1 0 0 1 1-.25 11.4 11.4 0 0 0 3.6.57 1 1 0 0 1 1 1V20a1 1 0 0 1-1 1A17 17 0 0 1 3 4a1 1 0 0 1 1-1h3.5a1 1 0 0 1 1 1c0 1.25.2 2.45.57 3.57a1 1 0 0 1-.25 1z"/></svg>
          555 210 4471
        </li>
        <li class="contact__item">
          <svg class="icon" viewBox="0 0 24 24"><path d="M7 1h10a2 2 0 0 1 2 2v18a2 2 0 0 1-2 2H7a2 2 0 0 1-2-2V3a2 2 0 0 1 2-2zm0 3v14h10V4zm5 15.2a1.2 1.2 0 1 0 0 2.4 1.2 1.2 0 0 0 0-2.4z"/></svg>
          555 362 8190
        </li>
        <li class="contact__item">
          <svg class="icon" viewBox="0 0 24 24"><path d="M6 2h12v6H6zM3 9h18a2 2 0 0 1 2 2v7h-4v4H5v-4H1v-7a2 2 0 0 1 2-2zm4 7v4h10v-4z"/></svg>
          555 784 3025
        </li>
        <li class="contact__item">
          <svg class="icon" viewBox="0 0 24 24"><path d="M2 5h20v14H2zm2 2v.5l8 5 8-5V7l-8 5z"/></svg>
          nadia@lumarawellness.com
        </li>
        <li class="contact__item">
          <svg class="icon" viewBox="0 0 24 24"><path d="M12 2a10 10 0 1 0 0 20 10 10 0 0 0 0-20zm6.9 9h-3a15 15 0 0 0-1.3-6A8 8 0 0 1 18.9 11zM12 4.1c.9 1.3 1.7 3.6 1.9 6.9h-3.8c.2-3.3 1-5.6 1.9-6.9zM9.4 5a15 15 0 0 0-1.3 6h-3A8 8 0 0 1 9.4 5zM5.1 13h3a15 15 0 0 0 1.3 6A8 8 0 0 1 5.1 13zm6.9 6.9c-.9-1.3-1.7-3.6-1.9-6.9h3.8c-.2 3.3-1 5.6-1.9 6.9zm2.6-.9a15 15 0 0 0 1.3-6h3a8 8 0 0 1-4.3 6z"/></svg>
          www.lumarawellness.com
        </li>
      </ul>
    </div>
    <p class="address">
      <svg class="icon" viewBox="0 0 20 24"><path d="M10 0a8 8 0 0 0-8 8c0 6 8 16 8 16s8-10 8-16a8 8 0 0 0-8-8zm0 11a3 3 0 1 1 0-6 3 3 0 0 1 0 6z"/></svg>
      2140 Willow Crest Drive Juneau, Alaska 99801
    </p>
  </section>
</main>
</body>
</html>
```